Design for an iOS and Android app managing shopping list

The app allows you to keep manage shopping lists, each shopping list being made of items to buy...
We need a design for the 3 screens of the app:
a) global view showing list of (shopping) list
b) form enabling to edit the name of a (shopping) list
c) detailed view listing the contents/items of a (shopping) list
d) 1 text page [not illustrated]
2 "alerts" items are also to be designed: confirm and error pop ups.
No specific guidelines, nor logo or whatever.
It will be a free app distributed on iOS and Androïd.
We just want to make it looking nice & very usable for end users.

```html
<!DOCTYPE html>
<html lang="en">
<head>
<meta charset="utf-8">
<title>Shopping Lists – Remove list confirmation</title>
<link href="https://fonts.googleapis.com/css2?family=Open+Sans:wght@300;400;600;700&display=swap" rel="stylesheet">
<style>
  :root {
    --stage: #33363b;
    --screen-bg: #f2f2f2;
    --row-line: #dcdcdc;
    --row-text: #8a8a8a;
    --header: #1f6f8f;
    --header-text: #ffffff;
    --scrim: rgba(0, 0, 0, 0.68);
    --dialog-bg: #f7f7f7;
    --dialog-title: #333333;
    --dialog-text: #555555;
    --cancel: #5a74f4;
    --delete: #ff3c3a;
    --icon: #8a8a8a;
  }
  * { box-sizing: border-box; margin: 0; padding: 0; }
  html, body {
    width: 1200px; height: 900px; overflow: hidden;
    background: var(--stage);
    font-family: "Open Sans", Arial, sans-serif;
  }
  .screen {
    position: absolute; left: 400px; top: 80px;
    width: 400px; height: 740px;
    background: var(--screen-bg);
    overflow: hidden;
  }
  .status-bar {
    height: 26px; background: var(--header);
    display: flex; justify-content: flex-end; align-items: center; gap: 8px;
    padding: 0 12px; color: var(--header-text); font-size: 12px;
  }
  .app-bar {
    height: 56px; background: var(--header);
    display: flex; justify-content: space-between; align-items: center;
    padding: 0 16px; color: var(--header-text);
    font-size: 16px; font-weight: 300; letter-spacing: 0.5px;
  }
  .back-link { display: flex; align-items: center; gap: 6px; }
  .lists { list-style: none; }
  .list-row {
    height: 64px; display: flex; justify-content: space-between; align-items: center;
    padding: 0 18px; border-bottom: 1px solid var(--row-line);
    color: var(--row-text); font-size: 16px; font-weight: 400;
  }
  .list-row.add-row { font-weight: 300; }
  .scrim { position: absolute; inset: 0; background: var(--scrim); }
  .dialog {
    position: absolute; left: 36px; top: 250px; width: 328px;
    background: var(--dialog-bg); border-radius: 3px;
    padding: 26px 18px 18px;
    box-shadow: 0 6px 20px rgba(0,0,0,0.35);
  }
  .dialog-title {
    font-size: 17px; font-weight: 700; color: var(--dialog-title);
    text-align: center; margin-bottom: 10px;
  }
  .dialog-text {
    font-size: 15px; color: var(--dialog-text); text-align: center;
    margin-bottom: 22px;
  }
  .dialog-actions { display: flex; gap: 10px; }
  .btn {
    flex: 1; height: 46px; border: none; border-radius: 3px;
    color: #fff; font-family: inherit; font-size: 14px; font-weight: 400;
    letter-spacing: 0.5px;
  }
  .btn-cancel { background: var(--cancel); }
  .btn-delete { background: var(--delete); }
</style>
</head>
<body>
  <main class="screen">
    <div class="status-bar">
      <svg width="14" height="12" viewBox="0 0 14 12"><polygon points="0,12 14,0 14,12" fill="#fff"/></svg>
      <svg width="10" height="13" viewBox="0 0 10 13"><rect x="3" y="0" width="4" height="2" fill="#fff"/><rect x="0" y="2" width="10" height="11" rx="1" fill="#fff"/></svg>
      <span class="clock">12:30</span>
    </div>
    <header class="app-bar">
      <span class="back-link">
        <svg width="9" height="14" viewBox="0 0 9 14"><polyline points="8,1 2,7 8,13" fill="none" stroke="#fff" stroke-width="1.5"/></svg>
        LISTS
      </span>
      <span class="about-link">ABOUT</span>
    </header>
    <ul class="lists">
      <li class="list-row add-row">Add a new shopping list</li>
      <li class="list-row"><span>Diner de se soir</span><svg class="trash" width="18" height="20" viewBox="0 0 18 20"><g fill="none" stroke="var(--icon)" stroke-width="1.5"><line x1="1" y1="4" x2="17" y2="4"/><rect x="6" y="1" width="6" height="3"/><rect x="3" y="4" width="12" height="15" rx="1"/><line x1="7" y1="8" x2="7" y2="16"/><line x1="11" y1="8" x2="11" y2="16"/></g></svg></li>
      <li class="list-row"><span>Menage</span><svg class="trash" width="18" height="20" viewBox="0 0 18 20"><g fill="none" stroke="var(--icon)" stroke-width="1.5"><line x1="1" y1="4" x2="17" y2="4"/><rect x="6" y="1" width="6" height="3"/><rect x="3" y="4" width="12" height="15" rx="1"/><line x1="7" y1="8" x2="7" y2="16"/><line x1="11" y1="8" x2="11" y2="16"/></g></svg></li>
      <li class="list-row"><span>Cadeaux de noel</span><svg class="trash" width="18" height="20" viewBox="0 0 18 20"><g fill="none" stroke="var(--icon)" stroke-width="1.5"><line x1="1" y1="4" x2="17" y2="4"/><rect x="6" y="1" width="6" height="3"/><rect x="3" y="4" width="12" height="15" rx="1"/><line x1="7" y1="8" x2="7" y2="16"/><line x1="11" y1="8" x2="11" y2="16"/></g></svg></li>
      <li class="list-row"><span>Diner de se soir</span><svg class="trash" width="18" height="20" viewBox="0 0 18 20"><g fill="none" stroke="var(--icon)" stroke-width="1.5"><line x1="1" y1="4" x2="17" y2="4"/><rect x="6" y="1" width="6" height="3"/><rect x="3" y="4" width="12" height="15" rx="1"/><line x1="7" y1="8" x2="7" y2="16"/><line x1="11" y1="8" x2="11" y2="16"/></g></svg></li>
      <li class="list-row"><span>Diner de se soir</span><svg class="trash" width="18" height="20" viewBox="0 0 18 20"><g fill="none" stroke="var(--icon)" stroke-width="1.5"><line x1="1" y1="4" x2="17" y2="4"/><rect x="6" y="1" width="6" height="3"/><rect x="3" y="4" width="12" height="15" rx="1"/><line x1="7" y1="8" x2="7" y2="16"/><line x1="11" y1="8" x2="11" y2="16"/></g></svg></li>
    </ul>
    <div class="scrim"></div>
    <section class="dialog" role="alertdialog" aria-labelledby="dialog-title">
      <h2 class="dialog-title" id="dialog-title">Remove the shopping list</h2>
      <p class="dialog-text">Would you like to delete shoping list?</p>
      <div class="dialog-actions">
        <button class="btn btn-cancel">CANCEL</button>
        <button class="btn btn-delete">DELETE</button>
      </div>
    </section>
  </main>
</body>
</html>
```